Business Card for High End Car Audio Company

Need a new bold business cards with our colors (blue, black, white, silver) and logo's. The card needs to have a high end look and would like the logo to be a large focus if possible. I've included old card for reference. The look was a little too simple for us. Needs nice double sided card.

Our company is a high end car audio company that produces subwoofers, speakers, and amplifiers for cars.

Target Market(s)

Car Audio

Industry/Entity Type

Electronic

Contact Information for Business Card

I included old business card for reference. Will need a template so I can use to create several cards for different people and departments.

Font styles to use
Serif
Sans Serif
Script

Colors
0555a3
ffffff
000000
9d9d9d

Requirements
Must have
• Logo, Info, Colors
Nice to have
• Bold and Elegant Design
Should not have
• Should not be plain.

```html
<!DOCTYPE html>
<html lang="en">
<head>
<meta charset="utf-8">
<title>Vantrell Audio Business Card</title>
<link href="https://fonts.googleapis.com/css2?family=Open+Sans:wght@400;600;700&display=swap" rel="stylesheet">
<style>
  :root {
    --page: #e9e9ec;
    --brand-blue: #0555a3;
    --navy: #1d3a86;
    --deep-blue: #1a4f9c;
    --ink: #2b2b2b;
    --silver: #9d9d9d;
    --silver-dark: #6f737a;
    --rule: #c9c9c9;
    --white: #ffffff;
  }
  * { margin: 0; padding: 0; box-sizing: border-box; }
  html, body { width: 1200px; height: 1000px; overflow: hidden; }
  body {
    background: var(--page);
    font-family: "Open Sans", Arial, sans-serif;
    position: relative;
  }
  .card {
    position: absolute;
    left: 266px;
    width: 666px;
    height: 397px;
    overflow: hidden;
    box-shadow: 0 4px 14px rgba(0,0,0,0.18);
  }
  .card--front { top: 74px; background: var(--white); }
  .card--back {
    top: 534px;
    background: radial-gradient(ellipse at 50% 45%, #2a80c8 0%, var(--brand-blue) 45%, #123f86 100%);
  }

  /* front */
  .brand-mark {
    position: absolute;
    top: 58px;
    right: 34px;
    display: flex;
    align-items: center;
    gap: 12px;
  }
  .brand-mark__dot {
    width: 46px; height: 46px; border-radius: 50%;
    background: var(--brand-blue);
  }
  .brand-mark__name {
    font-weight: 700;
    font-size: 34px;
    line-height: 1;
    letter-spacing: 1px;
    color: var(--brand-blue);
    text-transform: uppercase;
  }
  .person { position: absolute; left: 33px; top: 190px; }
  .person__name {
    font-weight: 600; font-size: 22px; color: var(--navy);
    letter-spacing: 0.3px; line-height: 1.1;
  }
  .person__title { font-size: 16px; color: var(--ink); margin-top: 3px; }
  .divider {
    position: absolute; left: 33px; top: 260px;
    width: 450px; height: 1px; background: var(--rule);
  }
  .address {
    position: absolute; left: 33px; top: 287px;
    font-size: 16px; line-height: 21px; color: var(--ink);
    font-style: normal;
  }
  .contacts {
    position: absolute; right: 32px; top: 249px;
    list-style: none; text-align: right;
    font-size: 16px; line-height: 24.5px; color: var(--ink);
  }
  .contacts li { display: flex; justify-content: flex-end; align-items: center; gap: 6px; }
  .contacts svg { width: 14px; height: 14px; fill: var(--deep-blue); flex: none; }
  .band { position: absolute; left: 0; bottom: 0; width: 666px; height: 28px; }

  /* back */
  .pattern-field {
    position: absolute; inset: 0;
    background: radial-gradient(ellipse at 50% 45%, rgba(255,255,255,0.05), rgba(0,0,0,0.08));
  }
  .back-name {
    position: absolute; left: 0; right: 0; top: 150px;
    text-align: center; color: var(--white);
    font-weight: 700; font-size: 46px; line-height: 50px;
    letter-spacing: 3px; text-transform: uppercase;
  }
</style>
</head>
<body>

<section class="card card--front" aria-label="Business card front">
  <div class="brand-mark">
    <span class="brand-mark__dot"></span>
    <span class="brand-mark__name">Vantrell Audio</span>
  </div>

  <div class="person">
    <h1 class="person__name">DANIEL HARTWELL</h1>
    <p class="person__title">Managing Director</p>
  </div>

  <div class="divider"></div>

  <address class="address">
    Level 14, 8 Harbour Point<br>
    Brookvale, 12, New South Wales
  </address>

  <ul class="contacts">
    <li>+ 000 000 0000
      <svg viewBox="0 0 14 14"><path d="M4 0h6a1 1 0 0 1 1 1v12a1 1 0 0 1-1 1H4a1 1 0 0 1-1-1V1a1 1 0 0 1 1-1zm0 2v8h6V2zm3 9.2a.9.9 0 1 0 0 1.8.9.9 0 0 0 0-1.8z"/></svg>
    </li>
    <li>+ 000 000 0000
      <svg viewBox="0 0 14 14"><path d="M1 5c0-2 2.5-3 6-3s6 1 6 3v1h-3V4.5H4V6H1zm2 2h8l2 5H1zm4 1.3a1.6 1.6 0 1 0 0 3.2 1.6 1.6 0 0 0 0-3.2z"/></svg>
    </li>
    <li>info@vantrellaudio.com
      <svg viewBox="0 0 14 14"><path d="M0 3h14v8H0zm1 1v.3l6 3.6 6-3.6V4zm0 1.5V10h12V5.5L7 9z"/></svg>
    </li>
    <li>www.vantrellaudio.com
      <svg viewBox="0 0 14 14"><path d="M7 0a7 7 0 1 0 0 14A7 7 0 0 0 7 0zm0 1.3c.8 0 1.6 1.6 1.9 4.2H5.1C5.4 2.9 6.2 1.3 7 1.3zM1.4 6.6h2.5c0 .9.1 1.7.3 2.4H1.8a5.6 5.6 0 0 1-.4-2.4zm3.8 0h3.6c0 .9-.1 1.7-.3 2.4h-3c-.2-.7-.3-1.5-.3-2.4zm4.9 0h2.5c0 .9-.2 1.7-.5 2.4h-2.3c.2-.7.3-1.5.3-2.4zM2.4 10.2h2.2c.3.9.7 1.7 1.1 2.3a5.7 5.7 0 0 1-3.3-2.3zm3.5 0h2.2c-.3 1.3-.7 2.3-1.1 2.4-.4-.1-.8-1.1-1.1-2.4z"/></svg>
    </li>
  </ul>

  <svg class="band" viewBox="0 0 666 28" preserveAspectRatio="none" aria-hidden="true">
    <defs>
      <linearGradient id="bandBlue" x1="0" x2="1">
        <stop offset="0" stop-color="#1d3a86"/>
        <stop offset="1" stop-color="#1577c0"/>
      </linearGradient>
      <linearGradient id="bandSilver" x1="0" x2="1">
        <stop offset="0" stop-color="#e8e9eb"/>
        <stop offset="1" stop-color="#6f737a"/>
      </linearGradient>
    </defs>
    <polygon points="0,0 325,0 290,28 0,28" fill="url(#bandBlue)"/>
    <polygon points="335,0 666,0 666,28 300,28" fill="url(#bandSilver)"/>
  </svg>
</section>

<section class="card card--back" aria-label="Business card back">
  <div class="pattern-field" role="img" aria-label="Faint repeating brand pattern over the blue background"></div>
  <p class="back-name">Vantrell<br>Audio</p>
</section>

</body>
</html>
```